LOLU Baby Massage Classes - flyer to make a difference

I need a single page flyer, preferably single page, to hand out to doctors, medical centres and parents. To also leave on counters of establishments.
It is to promote my baby massage classes. Mums can get together with other mums and book a 5 week course to learn and discover the many benefits of baby massage.
Benefits include: enhances bonding and attachment, understand non-verbal cues from your baby, helps with sleep patterns, help with immune system, increases vagal activity,relief from wind, colic or constipation to name some.

Baby age from birth to 12 months. Group classes or private sessions

I am a Professional Member and Certified by the Global Society of Newborn Touch (GSNT) GSNT Australia is Nationally Accredited and is endorsed by Crown Academy of Carers, the Southern Guild of Birth Attendants, The Southern Union of Daily Living Therapy Australia, The Southern Union of Bodywork Practitioner and is a full member of Wellmind Network Australia.

Class detail and availability contact is Petra Holm 0487 315 208 petra.joanne.holm@quillmail.example www.lolunewborntouch com.au facebook/comLOLUnewborntouch

My colour scheme is green and purple as you will see from my logo and website. I would like my flyer to be softer tones of either both colours or just one.

I will include some images you can choose from or show me any you think will fit in with baby massage. THANK YOU
Updates

Hi The size of my flyer is A6. Approx 150mms x 210mms and single sided. Thank you

Target Market(s)

mums and dads, groups, doctors, midwives

Industry/Entity Type

Medical

Font styles to use
Sans Serif

Colors
87d0c7
b09cc8

Requirements
Must have
• baby photo or photos, both my logo and the GSNT logo. The GSNT logo is to be small
• Baby Massage Classes (wording) is very important to catch the eye.
• Invitation to book a class or gather friends to book is next in importance
• Benefits is next
• The admin information ie.,membership, certification and endorsements are lesser and can be small.
• Contact information to be noticeable.
Nice to have
• If you have an idea, drawing or photo that would look better, please feel free to try it
Should not have
• should not be crowded with information all the same size

```html
<!DOCTYPE html>
<html lang="en">
<head>
<meta charset="utf-8">
<title>LOLU Baby Massage Classes</title>
<link href="https://fonts.googleapis.com/css2?family=Open+Sans:wght@400;600;700;800&display=swap" rel="stylesheet">
<style>
:root{
  --teal:#87d0c7;
  --purple:#b09cc8;
  --purple-deep:#8a70ad;
  --text-dark:#3d3d3d;
  --text-muted:#8a8a8a;
  --white:#ffffff;
  --photo-pink:#e9cbd8;
  --photo-lilac:#cdb6cf;
}
*{margin:0;padding:0;box-sizing:border-box}
html,body{width:857px;height:1200px;overflow:hidden;background:var(--white)}
body{font-family:"Open Sans",Arial,sans-serif;color:var(--text-dark)}
.flyer{position:relative;width:857px;height:1200px;overflow:hidden;background:var(--white)}
.hero-photo{position:absolute;left:0;top:0;width:857px;height:570px;
  background:radial-gradient(ellipse at 40% 35%,#f3dfe6 0%,var(--photo-pink) 35%,var(--photo-lilac) 70%,#a98aa6 100%)}
.hero-shade{position:absolute;left:305px;top:462px;width:552px;height:108px;background:rgba(90,60,85,.35)}
.partner-mark{position:absolute;left:584px;top:0;width:259px;height:240px;background:var(--white);
  display:flex;align-items:center;justify-content:center;gap:14px}
.partner-mark .dot{width:26px;height:26px;border-radius:50%;background:var(--purple-deep)}
.partner-mark .name{font-size:54px;font-weight:700;color:var(--purple-deep);letter-spacing:2px}
.title-block{position:absolute;left:0;top:462px;width:305px;height:283px;background:var(--teal);
  display:flex;align-items:center;justify-content:flex-end;padding-right:22px}
.title-block h1{color:var(--white);font-weight:800;font-size:52px;line-height:1.12;text-align:right}
.audience{position:absolute;left:326px;top:474px;color:var(--white);font-weight:700;font-size:25px;line-height:1.35}
.benefits{position:absolute;left:326px;top:586px;list-style:none}
.benefits li{display:flex;align-items:center;gap:14px;font-weight:700;font-size:18.5px;height:30.5px;color:var(--text-dark)}
.benefits li::before{content:"";width:15px;height:15px;background:var(--teal);flex:none}
.book-cta{position:absolute;left:88px;top:790px;display:flex;align-items:center;gap:26px}
.book-cta svg{width:76px;height:70px}
.book-cta h2{font-size:62px;font-weight:700;color:var(--purple);letter-spacing:-.5px}
.contact-band{position:absolute;left:0;top:885px;width:857px;height:118px;background:var(--purple);color:var(--white)}
.contact-band .label{position:absolute;left:50px;top:26px;font-size:21px;font-weight:700;line-height:1.4}
.contact-band .label span{font-weight:600}
.contact-band .phone{position:absolute;right:52px;top:14px;font-size:50px;font-weight:700;letter-spacing:.5px}
.contact-band .email{position:absolute;right:56px;top:80px;font-size:17px;font-weight:400}
.web-links{position:absolute;left:0;top:1011px;width:857px;text-align:center;font-size:17px;font-weight:700;color:var(--purple)}
.web-links .sep{margin:0 18px;font-weight:400}
.footer{position:absolute;left:50px;top:1090px;width:760px;display:flex;gap:26px;align-items:flex-start}
.client-mark{display:flex;align-items:center;gap:8px;flex:none;margin-top:12px}
.client-mark .dot{width:34px;height:34px;border-radius:50%;background:var(--teal)}
.client-mark .name{font-size:24px;font-weight:700;color:var(--teal)}
.credentials{font-size:11px;line-height:1.5;color:var(--text-muted)}
</style>
</head>
<body>
<main class="flyer">
  <div class="hero-photo" role="img" aria-label="Photo of a sleeping newborn baby wearing a lilac headband, lying on soft pink ruffled fabric"></div>
  <div class="hero-shade"></div>

  <div class="partner-mark"><span class="dot"></span><span class="name">GSNT</span></div>

  <section class="title-block"><h1>Baby<br>Massage<br>Classes</h1></section>

  <p class="audience">Baby age from birth to 12 months.<br>Group classes or private sessions.</p>

  <ul class="benefits">
    <li>Enhances bonding and attachment.</li>
    <li>Understand non-verbal cues from your baby.</li>
    <li>Helps with sleep patterns.</li>
    <li>Help with immune system.</li>
    <li>Increases vagal activity.</li>
    <li>Relief from wind, colic or constipation.</li>
  </ul>

  <div class="book-cta">
    <svg viewBox="0 0 76 70" aria-hidden="true">
      <rect x="4" y="12" width="54" height="54" rx="8" fill="none" stroke="#b09cc8" stroke-width="7"/>
      <path d="M18 36 L32 50 L70 8" fill="none" stroke="#87d0c7" stroke-width="9" stroke-linecap="round" stroke-linejoin="round"/>
    </svg>
    <h2>Book a class today!</h2>
  </div>

  <section class="contact-band">
    <p class="label">For class detail &amp; availability<br><span>contact Petra Holm</span></p>
    <p class="phone">0487 315 208</p>
    <p class="email">petra.joanne.holm@quillmail.example</p>
  </section>

  <p class="web-links">www.lolunewborntouch com.au<span class="sep">|</span>facebook/comLOLUnewborntouch</p>

  <footer class="footer">
    <div class="client-mark"><span class="dot"></span><span class="name">LOLU</span></div>
    <p class="credentials">I am a Professional Member and Certified by the Global Society of Newborn Touch (GSNT) GSNT Australia is Nationally Accredited and is endorsed by Crown Academy of Carers, the Southern Guild of Birth Attendants, The Southern Union of Daily Living Therapy Australia, The Southern Union of Bodywork Practitioner and is a full member of Wellmind Network Australia.</p>
  </footer>
</main>
</body>
</html>
```